WordPress Site Design and Code for Technology Consulting Startup

We need a WordPress design and code to a new site on Nimbo Vault. We have the logo and colors ready. The site will be a brochure site with a CONTACT page that contains a form that the prospective client fills out. The other pages would be ABOUT / SERVICES (3 option drop-down) / SUPPORT. The site should be appropriate for an IT Consulting / IT Managed Services / IT Project Management services in the Chicago area.

Target Market(s)

Across small, medium, large businesses.

Industry/Entity Type

Technology, network infrastructure, IT.

Coding

Coded - Design and coding required

Number of Pages Required

5+ page

Requirements
Nice to have
• I prefer mid-modern / simple / art deco / minimalist.

```html
<!DOCTYPE html>
<html lang="en">
<head>
<meta charset="utf-8">
<title>Kestrel — IT Support Chicago</title>
<link href="https://fonts.googleapis.com/css2?family=Poppins:wght@400;500;600;700&family=Roboto+Condensed:wght@300;400&display=swap" rel="stylesheet">
<style>
:root{
  --teal:#1f8fa3;
  --orange:#e9762b;
  --ink:#111111;
  --grey:#7a7a7a;
  --light:#f5f5f5;
  --field:#ececec;
  --dark:#141414;
  --btn:#2b2b2b;
  --line:#cfd8db;
}
*{margin:0;padding:0;box-sizing:border-box}
html,body{width:1200px;height:2957px;overflow:hidden;background:#fff}
body{font-family:'Poppins',sans-serif;color:var(--ink);position:relative}
.abs{position:absolute}
.body-copy{font-family:'Roboto Condensed',sans-serif;font-weight:300;color:var(--grey)}

/* header */
.site-header{position:absolute;top:0;left:0;width:1200px;height:63px;background:#fff;border-bottom:1px solid #e6e6e6}
.brand{position:absolute;left:234px;top:20px;display:flex;align-items:center;gap:8px}
.brand-mark{width:12px;height:12px;background:var(--teal)}
.brand-name{font-weight:600;font-size:20px;color:var(--teal);letter-spacing:1px}
.main-nav{position:absolute;left:478px;top:24px;display:flex;gap:14px;font-size:10px}
.header-divider{position:absolute;left:814px;top:12px;width:1px;height:40px;background:#e3e3e3}
.header-phone{position:absolute;left:845px;top:20px;display:flex;gap:12px;align-items:center}
.header-phone small{display:block;font-size:8px;color:var(--teal)}
.header-phone strong{font-size:13px;font-weight:500}

/* hero */
.hero{position:absolute;top:63px;left:0;width:1200px;height:504px;background:linear-gradient(135deg,#3b4549 0%,#28333a 45%,#3d4448 100%)}
.hero-photo{position:absolute;inset:0;background:linear-gradient(160deg,rgba(20,30,35,.55),rgba(60,68,72,.2))}
.hero-title{position:absolute;top:184px;width:100%;text-align:center;color:#fff;font-size:34px;font-weight:500;line-height:41px}
.hero-btn{position:absolute;left:555px;top:286px;width:90px;height:32px;background:var(--teal);color:#fff;font-size:10px;letter-spacing:.5px;display:flex;align-items:center;justify-content:center}
.hero-arrow{position:absolute;top:244px}
.hero-dots{position:absolute;top:477px;left:587px;display:flex;gap:6px}
.hero-dots i{width:4px;height:4px;border-radius:50%;background:rgba(255,255,255,.5)}
.hero-dots i:first-child{background:#fff}

/* about */
.about-title{position:absolute;left:262px;top:692px;font-size:24px;font-weight:700;line-height:30px}
.about-text{position:absolute;left:262px;top:802px;width:322px;font-size:11px;line-height:20.3px}
.about-photo{position:absolute;left:620px;top:626px;width:315px;height:361px;border-radius:48% 52% 46% 54%/50% 45% 55% 50%;background:radial-gradient(circle at 55% 45%,#d8c3ad 0%,#a99684 40%,#8c8d8f 70%,#e9e9e9 100%)}

/* history */
.history{position:absolute;top:990px;left:0;width:1200px;height:225px;background:var(--light)}
.history h2{position:absolute;left:262px;top:66px;font-size:24px;font-weight:700}
.history p{position:absolute;left:262px;top:113px;width:676px;font-size:11px;line-height:20.3px}

/* services */
.services h2{position:absolute;top:1266px;width:1200px;text-align:center;font-size:24px;font-weight:700}
.service-line{position:absolute;top:1344px;left:375px;width:449px;height:1px;background:var(--line)}
.service{position:absolute;top:1325px;width:200px;text-align:center}
.service-icon{width:40px;height:40px;border-radius:50%;background:var(--teal);margin:0 auto;display:flex;align-items:center;justify-content:center}
.service h3{margin-top:11px;font-size:14px;font-weight:600}
.service p{margin-top:16px;font-size:11px;line-height:20.5px}
.service .price{margin-top:9px;font-size:13px;font-weight:400;color:#333}
.pill{margin:12px auto 0;width:98px;height:30px;border-radius:15px;background:var(--teal);color:#fff;font-size:8.5px;display:flex;align-items:center;justify-content:center;gap:3px}

/* staff */
.staff{position:absolute;top:1598px;left:0;width:1200px;height:510px;background:var(--light)}
.staff h2{position:absolute;top:50px;width:100%;text-align:center;font-size:32px;font-weight:700}
.staff .lead{position:absolute;top:104px;left:410px;width:380px;text-align:center;font-size:11px;line-height:18px}
.member{position:absolute;width:150px;text-align:center}
.avatar{width:132px;height:132px;border-radius:50%;margin:0 auto}
.member h4{margin-top:18px;font-size:11.5px;font-weight:600}
.member .role{font-size:8px;margin-top:3px}
.member p{margin-top:10px;font-size:9px;line-height:17px}
.socials{display:flex;justify-content:center;gap:14px;margin-top:13px}
.socials i{width:6px;height:6px;border-radius:50%;background:#222}

/* contact */
.contact-photo{position:absolute;left:262px;top:2170px;width:266px;height:333px;border-radius:44% 56% 48% 52%/46% 48% 52% 54%;background:radial-gradient(circle at 50% 65%,#c98c55 0%,#9a6a44 40%,#6d5e55 70%,#ececec 100%)}
.contact-card{position:absolute;left:532px;top:2170px;width:405px;height:333px;background:#fff;box-shadow:0 0 12px rgba(0,0,0,.07)}
.contact-card h2{position:absolute;top:42px;width:100%;text-align:center;font-size:19px;font-weight:600}
.field{position:absolute;height:35px;background:var(--field);border-radius:4px;font-size:9.5px;color:#444;padding-left:11px;display:flex;align-items:center}
.send{position:absolute;left:264px;top:264px;width:110px;height:32px;background:var(--btn);color:#fff;font-size:8.5px;font-weight:600;letter-spacing:.4px;display:flex;align-items:center;justify-content:center}

/* ticket */
.ticket{position:absolute;top:2566px;left:0;width:1200px;height:69px;background:var(--light)}
.ticket span{position:absolute;left:395px;top:25px;font-size:15px;font-weight:400;color:#222}
.ticket svg{position:absolute;left:670px;top:24px}
.ticket .support{position:absolute;left:769px;top:17px;width:82px;height:37px;background:var(--btn);color:#fff;font-size:9px;font-weight:600;display:flex;align-items:center;justify-content:center}

/* footer */
.site-footer{position:absolute;top:2635px;left:0;width:1200px;height:322px;background:var(--dark);color:#fff}
.footer-brand{position:absolute;top:44px;width:100%;text-align:center;font-size:28px;font-weight:600;letter-spacing:3px}
.footer-rule{position:absolute;left:262px;width:676px;height:1px;background:#2e2e2e}
.footer-info{position:absolute;top:142px;display:flex;gap:10px}
.footer-info h5{font-size:13px;font-weight:600}
.footer-info p{font-size:8.5px;line-height:14px;margin-top:4px;color:#ddd}
.footer-nav{position:absolute;top:231px;width:100%;display:flex;justify-content:center;gap:13px;font-size:8px}
.footer-social{position:absolute;top:275px;width:100%;display:flex;justify-content:center;gap:18px}
.footer-social i{width:7px;height:7px;border-radius:50%;background:#fff}
.copyright{position:absolute;top:302px;width:100%;text-align:center;font-size:7.5px;color:#bbb}
</style>
</head>
<body>

<header class="site-header">
  <div class="brand"><span class="brand-mark"></span><span class="brand-name">KESTREL</span></div>
  <nav class="main-nav"><span>Home</span><span>About Us</span><span>Escape The Cycle</span><span>PlayBooks</span><span>Contact Us</span></nav>
  <div class="header-divider"></div>
  <div class="header-phone">
    <svg width="20" height="20" viewBox="0 0 24 24"><path d="M6.6 10.8a15.1 15.1 0 0 0 6.6 6.6l2.2-2.2c.3-.3.7-.4 1-.2 1.1.4 2.3.6 3.6.6.6 0 1 .4 1 1V20c0 .6-.4 1-1 1A17 17 0 0 1 3 4c0-.6.4-1 1-1h3.5c.6 0 1 .4 1 1 0 1.3.2 2.5.6 3.6.1.3 0 .7-.2 1z" fill="#111"/></svg>
    <div><small>Phone Number</small><strong>0200 555 01 23</strong></div>
  </div>
</header>

<section class="hero">
  <div class="hero-photo" role="img" aria-label="Looking up at glass office towers against a grey sky"></div>
  <h1 class="hero-title">IT Support Chicago, IL<br>Businesses Rely On</h1>
  <div class="hero-btn">READ MORE</div>
  <svg class="hero-arrow" style="left:34px" width="14" height="20" viewBox="0 0 14 20"><path d="M10 3 3 10l7 7" fill="none" stroke="#fff" stroke-width="2.5"/></svg>
  <svg class="hero-arrow" style="left:1154px" width="14" height="20" viewBox="0 0 14 20"><path d="m4 3 7 7-7 7" fill="none" stroke="#fff" stroke-width="2.5"/></svg>
  <div class="hero-dots"><i></i><i></i><i></i></div>
</section>

<section class="about">
  <h2 class="about-title">IT COMPANY<br>BASED IN<br>CHICAGO AREA</h2>
  <p class="about-text body-copy">Sed egestas, ante et vulputate volutpat, eros pede semper est, vitae luctus metus libero eu augue. Morbi purus libero, faucibus adipiscing, commodo quis, gravida id, est. Sed lectus. Praesent elementum hendrerit tortor. Sed semper lorem at felis. Vestibulum volutpat, lacus a ultrices sagittis, mi neque euismod dui, eu pulvinar nunc sapien ornare nisl. Phasellus pede arcu, dapibus eu, fermentum et, dapibus sed, urna.</p>
  <div class="about-photo" role="img" aria-label="Smiling consultant with glasses in a brushed-edge frame over a city backdrop"></div>
</section>

<section class="history">
  <h2>COMPANY HISTORY</h2>
  <p class="body-copy">Sed egestas, ante et vulputate volutpat, eros pede semper est, vitae luctus metus libero eu augue. Morbi purus libero, faucibus adipiscing, commodo quis, gravida id, est. Sed lectus. Praesent elementum hendrerit tortor. Sed semper lorem at felis. Vestibulum volutpat, lacus a ultrices sagittis, mi neque euismod dui, eu pulvinar nunc sapien ornare nisl. Phasellus pede arcu, dapibus eu, fermentum et, dapibus sed, urna.</p>
</section>

<section class="services">
  <h2>SERVICES</h2>
  <div class="service-line"></div>
  <div class="service" style="left:275px">
    <div class="service-icon"><svg width="20" height="20" viewBox="0 0 20 20"><rect x="3" y="4" width="14" height="9" fill="none" stroke="#fff" stroke-width="1.6"/><path d="M1 16h18" stroke="#fff" stroke-width="1.8"/></svg></div>
    <h3>Total IT</h3>
    <p class="body-copy">Lorem insum dolor amet consec tetur adiriscin elit eiusmod temsor incididunt masna alirua enim veniam nostrud.</p>
    <div class="price">$20/Device Managed</div>
    <div class="pill">PREVIEW MORE <span>&rarr;</span></div>
  </div>
  <div class="service" style="left:500px">
    <div class="service-icon"><svg width="20" height="20" viewBox="0 0 20 20"><path d="M3 10 10 4l7 6M5 9v7h10V9" fill="none" stroke="#fff" stroke-width="1.6"/></svg></div>
    <h3>Managed IT</h3>
    <p class="body-copy">Lorem insum dolor amet consec tetur adiriscin elit eiusmod temsor incididunt masna alirua enim veniam nostrud.</p>
    <div class="price">$30/Device Managed</div>
    <div class="pill">PREVIEW MORE <span>&rarr;</span></div>
  </div>
  <div class="service" style="left:724px">
    <div class="service-icon"><svg width="22" height="22" viewBox="0 0 22 22"><circle cx="11" cy="11" r="8" fill="none" stroke="#fff" stroke-width="1.5"/><ellipse cx="11" cy="11" rx="3.5" ry="8" fill="none" stroke="#fff" stroke-width="1.3"/><path d="M3 11h16M4.5 7h13M4.5 15h13" stroke="#fff" stroke-width="1.2"/></svg></div>
    <h3>Intelligent IT</h3>
    <p class="body-copy">Lorem insum dolor amet consec tetur adiriscin elit eiusmod temsor incididunt masna alirua enim veniam nostrud.</p>
    <div class="price">$50/Device Managed</div>
    <div class="pill">PREVIEW MORE <span>&rarr;</span></div>
  </div>
</section>

<section class="staff">
  <h2>Staff Information</h2>
  <p class="lead body-copy">Sabori aliruid commodi conseruatur autem resreh enderit volustate velit esse nihil conser illum dolorem fusiat voluntas sariatur.</p>
  <div class="member" style="left:264px;top:172px">
    <div class="avatar" role="img" aria-label="Portrait of a staff member in a suit" style="background:radial-gradient(circle at 50% 40%,#d7b59a,#6d8a5a 75%)"></div>
    <h4>Daniel Hart</h4><div class="role body-copy">Gynecology</div>
    <p class="body-copy">Lorem insum dolor amet consec tetur adiris elit eiusm temsor incidi dolore masna exceurs.</p>
    <div class="socials"><i></i><i></i><i></i><i></i></div>
  </div>
  <div class="member" style="left:437px;top:172px">
    <div class="avatar" role="img" aria-label="Portrait of a smiling staff member" style="background:radial-gradient(circle at 50% 45%,#e2b996,#c08d5c 75%)"></div>
    <h4>Daniel Hart</h4><div class="role body-copy">Gynecology</div>
    <p class="body-copy">Lorem insum dolor amet consec tetur adiris elit eiusm temsor incidi dolore masna exceurs.</p>
    <div class="socials"><i></i><i></i><i></i><i></i></div>
  </div>
  <div class="member" style="left:611px;top:172px">
    <div class="avatar" role="img" aria-label="Portrait of a staff member wearing a hat and glasses" style="background:radial-gradient(circle at 50% 50%,#cfb199,#4a4a52 75%)"></div>
    <h4>Daniel Hart</h4><div class="role body-copy">Gynecology</div>
    <p class="body-copy">Lorem insum dolor amet consec tetur adiris elit eiusm temsor incidi dolore masna exceurs.</p>
    <div class="socials"><i></i><i></i><i></i><i></i></div>
  </div>
  <div class="member" style="left:785px;top:172px">
    <div class="avatar" role="img" aria-label="Portrait of a bearded staff member in a blue suit" style="height:142px;border-radius:50% 50% 48% 48%;background:radial-gradient(circle at 50% 35%,#c79c7f,#2f4f80 72%,#e8eaee 100%)"></div>
    <h4>Daniel Hart</h4><div class="role body-copy">Gynecology</div>
    <p class="body-copy">Lorem insum dolor amet consec tetur adiris elit eiusm temsor incidi dolore masna exceurs.</p>
    <div class="socials"><i></i><i></i><i></i><i></i></div>
  </div>
</section>

<section class="contact">
  <div class="contact-photo" role="img" aria-label="Person working on a laptop at a wooden table in a brick office"></div>
  <form class="contact-card">
    <h2>Contact Form</h2>
    <div class="field" style="left:32px;top:79px;width:166px">Your Name</div>
    <div class="field" style="left:208px;top:79px;width:166px">Your Surname</div>
    <div class="field" style="left:32px;top:125px;width:166px">Company Name</div>
    <div class="field" style="left:208px;top:125px;width:166px">Email Address</div>
    <div class="field" style="left:32px;top:170px;width:342px">Subject</div>
    <div class="field" style="left:32px;top:216px;width:342px">Message</div>
    <div class="send">SEND MESSAGE &rarr;</div>
  </form>
</section>

<section class="ticket">
  <span>START A NEW SERVICE TICKET</span>
  <svg width="30" height="16" viewBox="0 0 30 16"><path d="M1 8h27M21 2l7 6-7 6" fill="none" stroke="#222" stroke-width="1.8"/></svg>
  <div class="support">SUPPORT</div>
</section>

<footer class="site-footer">
  <div class="footer-brand">KESTREL</div>
  <div class="footer-rule" style="top:113px"></div>
  <div class="footer-info" style="left:264px">
    <svg width="16" height="20" viewBox="0 0 16 20"><path d="M8 19s6-6.5 6-11A6 6 0 0 0 2 8c0 4.5 6 11 6 11z" fill="none" stroke="#fff" stroke-width="1.4"/><circle cx="8" cy="8" r="2.2" fill="none" stroke="#fff" stroke-width="1.3"/></svg>
    <div><h5>Address</h5><p>4120 Lakeview Ave<br>Northbrook<br>United States</p></div>
  </div>
  <div class="footer-info" style="left:500px">
    <svg width="14" height="20" viewBox="0 0 14 20"><rect x="2" y="1" width="10" height="18" rx="1.5" fill="none" stroke="#fff" stroke-width="1.4"/><path d="M6 16h2" stroke="#fff" stroke-width="1.4"/></svg>
    <div><h5>Phone</h5><p>(555) 014-2290</p></div>
  </div>
  <div class="footer-info" style="left:737px">
    <svg width="20" height="16" viewBox="0 0 20 16"><rect x="1" y="2" width="18" height="12" fill="none" stroke="#fff" stroke-width="1.3"/><path d="m1 2 9 7 9-7" fill="none" stroke="#fff" stroke-width="1.3"/></svg>
    <div><h5>Email</h5><p>info@kestrelit.com</p></div>
  </div>
  <div class="footer-rule" style="top:210px"></div>
  <nav class="footer-nav"><span>Home</span><span>About Us</span><span>Escape The Cycle</span><span>PlayBooks</span><span>Contact Us</span></nav>
  <div class="footer-social"><i></i><i></i><i></i></div>
  <div class="copyright">© 2023 Kestrel | All Rights Reserved</div>
</footer>

</body>
</html>
```